Country House in Italy Needs a Business Card Design

We need a business card design for “Casale del Ruscello”, a modern concept of a Farm Holidays/Country House to be opened in central Italy.
Attached is the company logo you did for us in the past.
Please
- create a double-sided business card design
- on the back I would like to have the logo
- on the front the copy
Copy on card:
o Casale del Ruscello
o Address: Via Fontalba, 14
Cingoli (MC), Italy
o Website: www.casaledelruscello.it
o Email: info@casaledelruscello.it
o my name : Lucilla
o my mobile phone number: +39 347 8124591
In the distribution of information keep in mind the possible inclusion also of a landline telephone number (currently not available / existing).
WE WOULD LIKE TO HAVE A MODERN, PROFFESIONAL, OUT OF THE BOX BUSINESS CARD. BE AS CREATIVE AS YOU WOULD LIKE.

```html
<!DOCTYPE html>
<html lang="it">
<head>
<meta charset="utf-8">
<title>Casale del Ruscello – Business Card</title>
<link rel="stylesheet" href="https://fonts.googleapis.com/css2?family=Cormorant+Garamond:wght@400&family=Exo+2:wght@400;600&display=swap">
<style>
  :root {
    --bg: #ece6dc;
    --frame: #5e4630;
    --paper: #ffffff;
    --orange: #f07636;
    --strip: #e4e4e4;
    --ink: #4a3a2c;
    --muted: #5b5b5b;
    --icon: #3d3d3d;
  }
  * { box-sizing: border-box; margin: 0; padding: 0; }
  html, body { width: 1073px; height: 1200px; overflow: hidden; }
  body {
    background: var(--bg);
    font-family: "Exo 2", sans-serif;
    position: relative;
  }
  .card {
    position: absolute;
    background: var(--frame);
    box-shadow: 0 10px 28px rgba(60, 40, 20, .18);
  }
  .card__paper {
    position: absolute;
    inset: 22px;
    background: var(--paper);
    border-radius: 40px / 14px;
    overflow: hidden;
  }
  /* Back side: portrait, brand only */
  .card--back { left: 356px; top: 40px; width: 360px; height: 570px; }
  .card--back .brand {
    position: absolute; left: 0; right: 0; top: 200px;
    display: flex; flex-direction: column; align-items: center; gap: 22px;
  }
  .brand__dot {
    width: 92px; height: 92px; border-radius: 50%;
    background: var(--orange);
  }
  .brand__name {
    font-family: "Cormorant Garamond", serif;
    font-weight: 400;
    color: var(--ink);
    font-size: 34px;
    letter-spacing: .5px;
    white-space: nowrap;
  }
  /* Front side: landscape, details */
  .card--front { left: 156px; top: 660px; width: 760px; height: 480px; }
  .card--front .brand {
    position: absolute; left: 60px; top: 58px;
    display: flex; align-items: center; gap: 20px;
  }
  .card--front .brand__dot { width: 70px; height: 70px; }
  .card--front .brand__name { font-size: 36px; }
  .contacts {
    position: absolute; left: 64px; top: 170px;
    display: flex; flex-direction: column; gap: 14px;
    list-style: none;
  }
  .contact { display: flex; align-items: center; gap: 12px; }
  .contact__icon {
    width: 26px; height: 26px; border-radius: 4px;
    background: var(--icon);
    display: flex; align-items: center; justify-content: center;
    flex: none;
  }
  .contact__text {
    font-size: 14px; line-height: 1.3; color: var(--muted);
  }
  .role-strip {
    position: absolute; left: 0; right: 0; bottom: 86px; height: 40px;
    background: var(--strip);
    display: flex; align-items: center; justify-content: flex-end;
    padding-right: 40px;
  }
  .role {
    font-size: 15px; font-weight: 600; letter-spacing: 3px;
    color: var(--muted); text-transform: uppercase;
  }
  .name-band {
    position: absolute; left: 0; right: 0; bottom: 0; height: 86px;
    background: var(--orange);
    display: flex; align-items: center; justify-content: flex-end;
    padding-right: 40px;
  }
  .person {
    font-size: 38px; font-weight: 600; letter-spacing: 3px;
    color: #fff; text-transform: uppercase;
  }
</style>
</head>
<body>

  <section class="card card--back" aria-label="Card back">
    <div class="card__paper">
      <div class="brand">
        <span class="brand__dot"></span>
        <span class="brand__name">Casale del Ruscello</span>
      </div>
    </div>
  </section>

  <section class="card card--front" aria-label="Card front">
    <div class="card__paper">
      <div class="brand">
        <span class="brand__dot"></span>
        <span class="brand__name">Casale del Ruscello</span>
      </div>

      <ul class="contacts">
        <li class="contact">
          <span class="contact__icon">
            <svg width="14" height="14" viewBox="0 0 24 24"><path fill="#fff" d="M6.6 10.8a15.1 15.1 0 0 0 6.6 6.6l2.2-2.2a1 1 0 0 1 1-.25 11.4 11.4 0 0 0 3.6.57 1 1 0 0 1 1 1V20a1 1 0 0 1-1 1A17 17 0 0 1 3 4a1 1 0 0 1 1-1h3.5a1 1 0 0 1 1 1c0 1.25.2 2.45.57 3.57a1 1 0 0 1-.25 1z"/></svg>
          </span>
          <span class="contact__text">+39 347 8124591</span>
        </li>
        <li class="contact">
          <span class="contact__icon">
            <svg width="14" height="14" viewBox="0 0 24 24"><path fill="#fff" d="M3 5h18v14H3z M3 5l9 7 9-7" stroke="#3d3d3d" stroke-width="1.6"/></svg>
          </span>
          <span class="contact__text">info@casaledelruscello.it<br>www.casaledelruscello.it</span>
        </li>
        <li class="contact">
          <span class="contact__icon">
            <svg width="14" height="14" viewBox="0 0 24 24"><path fill="#fff" d="M12 2a7 7 0 0 0-7 7c0 5.2 7 13 7 13s7-7.8 7-13a7 7 0 0 0-7-7zm0 9.5A2.5 2.5 0 1 1 12 6.5a2.5 2.5 0 0 1 0 5z"/></svg>
          </span>
          <span class="contact__text">Via Fontalba, 14<br>Cingoli (MC), Italy</span>
        </li>
      </ul>

      <div class="role-strip"><span class="role">General Manager</span></div>
      <div class="name-band"><span class="person">Lucilla Ferrante</span></div>
    </div>
  </section>

</body>
</html>
```